Harrowgate Supply Group Business Card Design

The Business Card will be one side only with Harrowgate Supplies Group Logo
Card should have:
Name
Title
Office phone Number
Cell Number
email address
Website
Street Address
Our Slogan is Rugged and Reliable
Looking for something that stands out from other business cards

Target Market(s)

Heavy equipment Lease Company

```html
<!DOCTYPE html>
<html lang="en">
<head>
<meta charset="utf-8">
<title>Harrowgate Supplies Group – Business Card</title>
<link href="https://fonts.googleapis.com/css2?family=Open+Sans:ital,wght@0,400;0,600;0,700;0,800;1,400;1,600&display=swap" rel="stylesheet">
<style>
  :root {
    --backdrop: #e4e4e4;
    --card-white: #ffffff;
    --brand-red: #e2061f;
    --brand-navy: #1f2a8a;
    --ink: #3a3a3a;
    --gradient-top: #c8102e;
    --gradient-mid: #8a3d66;
    --gradient-bottom: #3e3a8c;
    --on-dark: #ffffff;
  }
  * { box-sizing: border-box; margin: 0; padding: 0; }
  html, body {
    width: 1200px; height: 1200px; overflow: hidden;
    background: var(--backdrop);
    font-family: "Open Sans", Arial, sans-serif;
  }
  .canvas {
    width: 1200px; height: 1200px;
    display: flex; flex-direction: column; align-items: center; justify-content: center;
    gap: 60px;
  }
  .card {
    width: 700px; height: 400px; position: relative; overflow: hidden;
    box-shadow: 0 6px 18px rgba(0,0,0,.15);
  }

  /* Front */
  .card-front { background: var(--card-white); }
  .brand-block { position: absolute; top: 44px; left: 0; right: 0; text-align: center; }
  .brand-name {
    font-weight: 800; font-size: 34px; letter-spacing: .5px;
    color: var(--brand-red); text-transform: uppercase;
  }
  .slogan { margin-top: 4px; font-size: 16px; color: var(--brand-red); font-style: italic; }
  .person { position: absolute; top: 140px; left: 0; right: 0; text-align: center; }
  .person-name { font-weight: 800; font-size: 26px; color: var(--brand-red); }
  .person-title { font-size: 15px; color: var(--brand-navy); font-style: italic; margin-top: 2px; }
  .address { font-size: 15px; color: var(--ink); margin-top: 10px; }

  .contact-band {
    position: absolute; left: 0; right: 0; top: 270px; height: 100px;
    background: var(--brand-red);
    display: flex; align-items: center; justify-content: center;
  }
  .contact-band::before, .contact-band::after {
    content: ""; position: absolute; left: 0; right: 0; height: 1.5px; background: var(--on-dark);
  }
  .contact-band::before { top: 8px; }
  .contact-band::after { bottom: 8px; }
  .contact-col { display: flex; flex-direction: column; gap: 10px; padding: 0 22px; }
  .contact-col.left { align-items: flex-end; }
  .contact-col.right { align-items: flex-start; }
  .contact-divider { width: 1.5px; height: 58px; background: var(--on-dark); }
  .contact-item {
    display: flex; align-items: center; gap: 8px;
    color: var(--on-dark); font-size: 16px; font-weight: 600;
  }
  .contact-item svg { width: 16px; height: 16px; fill: var(--on-dark); flex: none; }

  /* Back */
  .card-back {
    background: linear-gradient(150deg, var(--gradient-top) 0%, var(--gradient-mid) 50%, var(--gradient-bottom) 100%);
    display: flex; flex-direction: column; align-items: center; justify-content: center; gap: 14px;
  }
  .back-brand { display: flex; align-items: center; gap: 16px; }
  .back-brand .mark { width: 22px; height: 22px; border-radius: 50%; background: var(--on-dark); }
  .back-brand .brand-name { color: var(--on-dark); font-size: 36px; }
  .back-web { color: var(--on-dark); font-size: 24px; font-style: italic; }
</style>
</head>
<body>
<main class="canvas">

  <section class="card card-front" aria-label="Business card front">
    <div class="brand-block">
      <div class="brand-name">Harrowgate Supplies Group</div>
      <div class="slogan">Rugged and Reliable</div>
    </div>
    <div class="person">
      <div class="person-name">JOHN DOE</div>
      <div class="person-title">Director</div>
      <div class="address">Dummy city, Dummy Country Land</div>
    </div>
    <div class="contact-band">
      <div class="contact-col left">
        <div class="contact-item">1-234-567890
          <svg viewBox="0 0 16 16" aria-hidden="true"><path d="M4 0h8a1 1 0 0 1 1 1v14a1 1 0 0 1-1 1H4a1 1 0 0 1-1-1V1a1 1 0 0 1 1-1zm1 2v10h6V2zm3 11a1 1 0 1 0 0 2 1 1 0 0 0 0-2z"/></svg>
        </div>
        <div class="contact-item">john@harrowgatesupply.com
          <svg viewBox="0 0 16 16" aria-hidden="true"><path d="M0 3h16v10H0zm1.5 1.2v.3L8 9l6.5-4.5v-.3zM1 5.8V12h14V5.8L8 10.5z"/></svg>
        </div>
      </div>
      <div class="contact-divider"></div>
      <div class="contact-col right">
        <div class="contact-item">
          <svg viewBox="0 0 16 16" aria-hidden="true"><path d="M3.6 1 6 3.6 4.6 5.4a9 9 0 0 0 6 6l1.8-1.4L15 12.4l-1.6 2.4C7 15 1 9 1.2 2.6z"/></svg>
          1-234-567890
        </div>
        <div class="contact-item">
          <svg viewBox="0 0 16 16" aria-hidden="true"><path d="M8 0a8 8 0 1 0 0 16A8 8 0 0 0 8 0zm5.9 7.3h-2.6a12 12 0 0 0-1-5 6.5 6.5 0 0 1 3.6 5zM8 1.5c.8 1 1.6 3 1.8 5.8H6.2C6.4 4.5 7.2 2.5 8 1.5zM5.7 2.3a12 12 0 0 0-1 5H2.1a6.5 6.5 0 0 1 3.6-5zM2.1 8.7h2.6a12 12 0 0 0 1 5 6.5 6.5 0 0 1-3.6-5zM8 14.5c-.8-1-1.6-3-1.8-5.8h3.6c-.2 2.8-1 4.8-1.8 5.8zm2.3-.8a12 12 0 0 0 1-5h2.6a6.5 6.5 0 0 1-3.6 5z"/></svg>
          www.harrowgatesupply.com
        </div>
      </div>
    </div>
  </section>

  <section class="card card-back" aria-label="Business card back">
    <div class="back-brand">
      <span class="mark" aria-hidden="true"></span>
      <span class="brand-name">Harrowgate Supplies Group</span>
    </div>
    <div class="back-web">www.harrowgatesupply.com</div>
  </section>

</main>
</body>
</html>
```